Design a visually appealing layout for our company mission and values. I want to create a visually appealing 1 page flyer that presents our company mission and values to clients as well as to our internal team/staff. We will utilize the 1 page flyer in internal and external presentations about our company. We will also use the flyer in sales proposals/marketing packages.

Target Market(s)

Internal team members as well as external prospective clients, existing clients & referral partners

Industry/Entity Type

Financial Service

Colors

Designer to choose colors to be used in the design.

Requirements
Must have
• Should reflect our company brand so I have included our Pantone panel, fonts etc. I have provided our company logo as well which should be part of the branded document
Nice to have
• I would like the presentation to be useable in different formats and to different audiences so something that is more graphic/visual heavy - otherwise it's a lot of words that people don't read.
• Would like to be able to easily include in our corporate template powerpoint presentation.

```html
<!DOCTYPE html>
<html lang="en">
<head>
<meta charset="UTF-8">
<title>Mission &amp; Values Flyer</title>
<link href="https://fonts.googleapis.com/css2?family=Montserrat:wght@400;500;700;800&family=Oswald:wght@600&display=swap" rel="stylesheet">
<style>
  :root{
    --blue:#1d5fa3;
    --blue-dark:#184e8a;
    --green:#7ab342;
    --green-soft:#cfe3b2;
    --gray:#58595b;
    --ink:#33343a;
    --paper:#ffffff;
    --bg:#e9eaec;
  }
  *{box-sizing:border-box;margin:0;padding:0}
  html,body{width:1200px;height:800px;overflow:hidden;background:var(--bg)}
  body{font-family:"Montserrat",sans-serif;color:var(--ink);position:relative}
  .flyer{position:absolute;left:310px;top:20px;width:580px;height:760px;background:var(--paper);box-shadow:0 4px 18px rgba(0,0,0,.15);overflow:hidden}

  .hero{position:absolute;left:0;top:0;width:100%;height:215px;
    background:linear-gradient(90deg,#ffffff 0%,#f3f7ee 30%,#cfe3b2 55%,#b8a98a 78%,#d9d4c8 100%)}
  .hero-fade{position:absolute;left:0;top:0;width:100%;height:215px;background:linear-gradient(180deg,rgba(255,255,255,0) 60%,#fff 100%)}

  .brand{position:absolute;left:34px;top:130px;display:flex;align-items:center;gap:10px}
  .brand-mark{width:14px;height:14px;background:var(--green)}
  .brand-name{font-weight:700;font-size:17px;color:var(--blue);line-height:1.15;letter-spacing:.5px}

  .title-ribbon{position:absolute;left:0;top:194px;height:46px;width:350px;
    background:linear-gradient(90deg,var(--green) 0 14px,var(--blue) 14px,var(--blue-dark));
    clip-path:polygon(0 0,100% 0,92% 100%,0 100%)}
  .title-ribbon h1{font-family:"Oswald",sans-serif;font-weight:600;font-size:30px;color:#fff;line-height:46px;padding-left:32px;letter-spacing:.5px}

  .mission{position:absolute;left:32px;top:252px;right:32px}
  .mission h2{font-size:15px;font-weight:800;color:var(--blue);letter-spacing:.5px}
  .mission p{font-size:12.5px;margin-top:3px;font-weight:500}

  .values{position:absolute;left:28px;right:28px;top:312px;height:378px;border:1.5px solid var(--green);border-radius:6px}
  .values-tab{position:absolute;left:-10px;top:-14px;height:28px;padding:0 28px 0 16px;background:var(--blue);color:#fff;font-weight:800;font-size:14px;line-height:28px;letter-spacing:.5px;clip-path:polygon(0 0,88% 0,100% 100%,0 100%)}
  .value-list{list-style:none;padding:22px 16px 0 16px}
  .value{display:flex;align-items:center;gap:14px;height:50px}
  .value-icon{flex:0 0 40px;width:40px;height:40px}
  .value h3{font-size:12.5px;font-weight:800;color:var(--blue)}
  .value p{font-size:9.6px;line-height:1.3;margin-top:1px}

  .footer-web{position:absolute;right:0;top:700px;height:22px;width:250px;border-top-left-radius:22px;
    background:linear-gradient(90deg,var(--green),var(--blue));color:#fff;font-size:11px;font-weight:700;display:flex;align-items:center;gap:6px;padding-left:26px}
  .footer-bar{position:absolute;left:0;right:0;top:722px;height:38px;background:var(--gray);display:flex;align-items:center;gap:36px;padding-left:34px;color:#fff;font-size:12px;font-weight:500;border-top:3px solid var(--blue)}
  .footer-bar span,.footer-web span{display:inline-flex;align-items:center;gap:6px}
</style>
</head>
<body>
<main class="flyer">
  <div class="hero" role="img" aria-label="Photo of a coin jar labelled retirement beside stacked coins on a soft green background"></div>
  <div class="hero-fade"></div>

  <div class="brand">
    <span class="brand-mark"></span>
    <span class="brand-name">HARBORLINE<br>RETIREMENT PARTNERS</span>
  </div>

  <div class="title-ribbon"><h1>MISSION &amp; VALUES</h1></div>

  <section class="mission">
    <h2>OUR MISSION:</h2>
    <p>To proactively support organizations and lead them toward a secure future.</p>
  </section>

  <section class="values">
    <div class="values-tab">WE VALUE:</div>
    <ul class="value-list">
      <li class="value">
        <svg class="value-icon" viewBox="0 0 40 40"><circle cx="20" cy="20" r="19" fill="#7ab342"/><circle cx="20" cy="20" r="16" fill="#1d5fa3"/><g fill="none" stroke="#fff" stroke-width="1.5"><circle cx="15" cy="16" r="3"/><circle cx="25" cy="16" r="3"/><path d="M9 27c1-4 4-6 6-6s5 2 6 6M19 27c1-4 4-6 6-6s5 2 6 6"/></g></svg>
        <div><h3>Teamwork:</h3><p>Collaborating with team members, clients and partners to maintain a high level of communication, accountability and engagement to achieve our common goals</p></div>
      </li>
      <li class="value">
        <svg class="value-icon" viewBox="0 0 40 40"><circle cx="20" cy="20" r="19" fill="#7ab342"/><circle cx="20" cy="20" r="16" fill="#1d5fa3"/><g fill="none" stroke="#fff" stroke-width="1.5"><path d="M11 28h18M13 28v-5M18 28v-8M23 28v-11M28 28v-14"/><path d="M12 20l6-5 4 3 7-7"/></g></svg>
        <div><h3>Financial Empowerment:</h3><p>We commit ourselves to providing the best retirement solutions to guide our clients toward financial freedom</p></div>
      </li>
      <li class="value">
        <svg class="value-icon" viewBox="0 0 40 40"><circle cx="20" cy="20" r="19" fill="#7ab342"/><circle cx="20" cy="20" r="16" fill="#1d5fa3"/><g fill="none" stroke="#fff" stroke-width="1.5"><circle cx="20" cy="17" r="6"/><path d="M17 25h6M18 28h4M20 8v2M11 17h2M27 17h2"/></g></svg>
        <div><h3>Knowledge:</h3><p>Our team of highly trained and credentialed experts work to educate and lead our clients toward success</p></div>
      </li>
      <li class="value">
        <svg class="value-icon" viewBox="0 0 40 40"><circle cx="20" cy="20" r="19" fill="#7ab342"/><circle cx="20" cy="20" r="16" fill="#1d5fa3"/><g fill="none" stroke="#fff" stroke-width="1.5"><circle cx="20" cy="20" r="8"/><path d="M16 20l3 3 5-6"/></g></svg>
        <div><h3>Proactivity:</h3><p>We hold ourselves accountable in anticipating regulatory changes and keeping you and your plan in compliance</p></div>
      </li>
      <li class="value">
        <svg class="value-icon" viewBox="0 0 40 40"><circle cx="20" cy="20" r="19" fill="#7ab342"/><circle cx="20" cy="20" r="16" fill="#1d5fa3"/><g fill="none" stroke="#fff" stroke-width="1.5"><circle cx="20" cy="16" r="4"/><path d="M12 29c1-5 4-8 8-8s7 3 8 8"/></g></svg>
        <div><h3>Dedication:</h3><p>We provide exceptional customer service and ensure that we are friendly, timely and responsive whenever corresponding with our clients</p></div>
      </li>
      <li class="value">
        <svg class="value-icon" viewBox="0 0 40 40"><circle cx="20" cy="20" r="19" fill="#7ab342"/><circle cx="20" cy="20" r="16" fill="#1d5fa3"/><g fill="none" stroke="#fff" stroke-width="1.5"><path d="M20 9l9 3v7c0 6-4 9-9 11-5-2-9-5-9-11v-7z"/><path d="M16 19l3 3 5-5"/></g></svg>
        <div><h3>Security:</h3><p>With an emphasis on high technological standards, we lead you toward peace of mind that your savings and investments are protected</p></div>
      </li>
      <li class="value">
        <svg class="value-icon" viewBox="0 0 40 40"><circle cx="20" cy="20" r="19" fill="#7ab342"/><circle cx="20" cy="20" r="16" fill="#1d5fa3"/><g fill="none" stroke="#fff" stroke-width="1.5"><circle cx="18" cy="18" r="6"/><path d="M22.5 22.5l6 6"/></g></svg>
        <div><h3>Transparency:</h3><p>We take pride in representing the retirement plan industry as an open, honest, and socially responsible firm with our clients</p></div>
      </li>
    </ul>
  </section>

  <div class="footer-web">
    <span><svg width="12" height="12" viewBox="0 0 12 12"><g fill="none" stroke="#fff" stroke-width="1"><circle cx="6" cy="6" r="5"/><path d="M1 6h10M6 1c2 2 2 8 0 10M6 1c-2 2-2 8 0 10"/></g></svg>www.harborlineretire.com</span>
  </div>
  <footer class="footer-bar">
    <span><svg width="12" height="12" viewBox="0 0 12 12"><path d="M2 1h2.5l1 3-1.5 1c.7 1.4 1.6 2.3 3 3l1-1.5 3 1V10c0 .6-.5 1-1 1C5 11 1 7 1 2c0-.5.4-1 1-1z" fill="#fff"/></svg>555.010.2468</span>
    <span><svg width="13" height="10" viewBox="0 0 13 10"><g fill="none" stroke="#fff" stroke-width="1.1"><rect x="0.6" y="0.6" width="11.8" height="8.8"/><path d="M0.6 0.6l5.9 5 5.9-5"/></g></svg>info@harborlineretire.com</span>
  </footer>
</main>
</body>
</html>
```